Modern two-sided business card for a general enterprise that improves the digital user experience.

Our company based in Switzerland covers all services of the digital customer relationship. We automate online ads to acquire new customers and program mobile apps for more efficient customer care in customer service. We employ specialists in marketing, business management, data science, graphic designers, copywriters, UI and programmers. The new business card is intended to show our comprehensive role and various offering of the entire customer journey.

Company Font: Futura
Main Color: # 283583
Secondary: #fcfaee (and gray variations)
Website: https://vko.example

As little address information as possible: company name, employee, mobile, email, company web & company phone.

Target Market(s)

C-Level (CEO, CIO, CTO), Head Sales, Head Marketing & Head Customer Service

Industry/Entity Type

Digital Marketing, Online-Marketing, Analytics

Contact Information for Business Card

Requirements
Must have
• Company logo type ": vko" only on one side

```html
<!DOCTYPE html>
<html lang="en">
<head>
<meta charset="utf-8">
<title>vko business card</title>
<link rel="stylesheet" href="https://fonts.googleapis.com/css2?family=Jost:wght@400;700&display=swap">
<style>
  :root {
    --brand-blue: #283583;
    --brand-blue-dark: #223070;
    --brand-blue-light: #2d3d96;
    --ink: #1d1d1f;
    --paper: #ffffff;
    --rule: #b9b9bd;
    --backdrop: #2b2b2d;
    --font-main: "Jost", "Futura", sans-serif;
  }
  * { box-sizing: border-box; margin: 0; padding: 0; }
  html, body { width: 1200px; height: 1015px; overflow: hidden; }
  body {
    background: var(--backdrop);
    font-family: var(--font-main);
    position: relative;
  }
  .card {
    position: absolute;
    left: 240px;
    width: 720px;
    height: 412px;
    box-shadow: 0 14px 30px rgba(0,0,0,0.55);
    overflow: hidden;
  }

  /* Front side: brand field only */
  .card-front { top: 70px; background: var(--brand-blue); }
  .front-texture {
    position: absolute; inset: 0;
    background: linear-gradient(135deg, var(--brand-blue-dark) 0%, var(--brand-blue) 55%, var(--brand-blue-light) 100%);
  }

  /* Back side */
  .card-back { top: 533px; background: var(--paper); }
  .back-wordmark {
    position: absolute;
    left: 0; width: 372px;
    top: 150px;
    text-align: center;
    color: var(--ink);
    font-weight: 700;
    font-size: 110px;
    line-height: 1;
  }
  .divider {
    position: absolute;
    left: 372px; top: 96px;
    width: 1px; height: 220px;
    background: var(--rule);
  }
  .contact {
    position: absolute;
    left: 400px; top: 96px;
    color: var(--ink);
  }
  .contact-name {
    color: var(--brand-blue);
    font-weight: 700;
    font-size: 27px;
    line-height: 1.2;
    margin-bottom: 14px;
  }
  .contact-list { list-style: none; }
  .contact-item {
    display: flex; align-items: center; gap: 10px;
    font-size: 16px;
    font-weight: 400;
    height: 28px;
  }
  .contact-icon { width: 22px; height: 22px; flex: none; }
  .contact-address {
    margin-top: 12px;
    font-size: 16px;
    font-weight: 400;
    line-height: 1.3;
  }
</style>
</head>
<body>
  <section class="card card-front" aria-label="Card front">
    <div class="front-texture" role="img" aria-label="Tone-on-tone embossed repeat pattern across the blue field"></div>
  </section>

  <section class="card card-back" aria-label="Card back">
    <div class="back-wordmark">vko</div>
    <div class="divider"></div>
    <div class="contact">
      <h1 class="contact-name">Lena Hartmann</h1>
      <ul class="contact-list">
        <li class="contact-item">
          <svg class="contact-icon" viewBox="0 0 22 22" aria-hidden="true"><circle cx="11" cy="11" r="11" fill="#283583"/><rect x="7.5" y="5" width="7" height="12" rx="1.5" fill="none" stroke="#fff" stroke-width="1.4"/><circle cx="11" cy="15" r="0.8" fill="#fff"/></svg>
          <span>044-555 010 200</span>
        </li>
        <li class="contact-item">
          <svg class="contact-icon" viewBox="0 0 22 22" aria-hidden="true"><circle cx="11" cy="11" r="11" fill="#283583"/><path d="M7 6.5c0 5 3.5 8.5 8.5 8.5l1-2-2.3-1.2-1 1c-1.5-.6-2.9-2-3.5-3.5l1-1L9.5 6z" fill="#fff"/></svg>
          <span>044-555 010 200</span>
        </li>
        <li class="contact-item">
          <svg class="contact-icon" viewBox="0 0 22 22" aria-hidden="true"><circle cx="11" cy="11" r="11" fill="#283583"/><rect x="5.5" y="7" width="11" height="8" fill="none" stroke="#fff" stroke-width="1.3"/><path d="M5.5 7l5.5 4.5L16.5 7" fill="none" stroke="#fff" stroke-width="1.3"/></svg>
          <span>info@vko.example</span>
        </li>
        <li class="contact-item">
          <svg class="contact-icon" viewBox="0 0 22 22" aria-hidden="true"><circle cx="11" cy="11" r="11" fill="#283583"/><circle cx="11" cy="11" r="5.5" fill="none" stroke="#fff" stroke-width="1.2"/><ellipse cx="11" cy="11" rx="2.4" ry="5.5" fill="none" stroke="#fff" stroke-width="1.1"/><path d="M5.5 11h11" stroke="#fff" stroke-width="1.1"/></svg>
          <span>www.vko.example</span>
        </li>
      </ul>
      <p class="contact-address">421, Address line goes here<br>45452,Country Name</p>
    </div>
  </section>
</body>
</html>
```